Bellwether Guild Forum Powerpoint Template

We need a Powerpoint template to use for a professional association called the Bellwether Guild Forum. The design should incorporate a logo that we will attach. We're looking for something clean, elegant, and professional. I'm attaching a sample Powerpoint file with 2 slides of content that we'd like to have designed so that they look good and incorporate the logo. The intention is that we can then take that template and create more content on our own.

Font styles to use
Sans Serif

```html
<!DOCTYPE html>
<html lang="en">
<head>
<meta charset="utf-8">
<title>Bellwether Guild Forum – Presentation Template</title>
<link href="https://fonts.googleapis.com/css2?family=Montserrat:wght@500;600;700;800&family=Open+Sans:wght@400;600&display=swap" rel="stylesheet">
<style>
:root{
  --navy:#0b2f7a;
  --deep:#082563;
  --blue:#1560c4;
  --sky:#2e8de0;
  --pale:#d9e7f7;
  --ink:#1d2433;
  --muted:#6b7385;
  --line:#d6dbe4;
  --stage:#f1f2f5;
  --white:#ffffff;
}
*{box-sizing:border-box;margin:0;padding:0}
html,body{width:1200px;height:4492px;overflow:hidden;background:var(--stage)}
body{font-family:"Open Sans",Arial,sans-serif;color:var(--ink)}
.canvas{position:relative;width:1200px;height:4492px;overflow:hidden;background:var(--stage)}
.slide{position:absolute;width:560px;height:316px;background:var(--white);overflow:hidden;box-shadow:0 2px 8px rgba(10,30,80,.12)}
.slide.hero{width:960px;height:540px;left:120px;top:110px;box-shadow:0 10px 30px rgba(10,30,80,.22)}
.abs{position:absolute}
.deco{position:absolute;left:0;top:0}
.logo{position:absolute;display:flex;align-items:center;gap:6px;font-family:"Montserrat",Arial,sans-serif;font-weight:700;font-size:7px;letter-spacing:.08em;text-transform:uppercase;color:var(--navy);white-space:nowrap}
.logo i{display:block;width:11px;height:11px;background:var(--blue)}
.logo.light{color:var(--white)}
.logo.light i{background:var(--white)}
.title{font-family:"Montserrat",Arial,sans-serif;font-weight:800;color:var(--navy);line-height:1.05;letter-spacing:-.01em}
.title.light{color:var(--white)}
.t-lg{font-size:30px}
.t-md{font-size:22px}
.t-sm{font-size:17px}
.t-sm b{color:var(--blue)}
.sub{font-family:"Montserrat",Arial,sans-serif;font-weight:500;font-size:13px;color:var(--blue);line-height:1.25}
.sub.light{color:var(--pale)}
.date{font-size:8px;color:var(--muted)}
.date.light{color:var(--pale)}
.body{font-size:7px;line-height:1.45;color:var(--muted)}
.body.light{color:var(--pale)}
.item-title{font-family:"Montserrat",Arial,sans-serif;font-weight:700;font-size:9px;color:var(--blue);line-height:1.15}
.item-title.light{color:var(--white)}
.pager{position:absolute;right:10px;bottom:10px;width:7px;height:7px;background:var(--blue)}
.pager.light{background:var(--white)}
.photo{position:absolute}
.ph-office{background:linear-gradient(135deg,#c9d3de,#8e9fb3 55%,#5d6f86)}
.ph-hands{background:linear-gradient(160deg,#e7ebf0,#b6c2cf 50%,#7d8ea3)}
.ph-tech{background:linear-gradient(135deg,#1b3b7a,#2f6fc7 50%,#0d2150)}
.ph-desk{background:linear-gradient(120deg,#eef1f4,#c7d0da 60%,#9aa8b8)}
.ph-blue{background:linear-gradient(135deg,#0f3f9a,#1d62c6 60%,#0a2a6e)}
.tbl{position:absolute;border-collapse:collapse;font-size:6.5px;color:var(--ink)}
.tbl th{background:var(--blue);color:var(--white);font-family:"Montserrat",Arial,sans-serif;font-weight:700;text-align:left;padding:5px 6px}
.tbl td{padding:4px 6px;border-bottom:1px solid var(--line)}
.tbl tr:nth-child(even) td{background:#f3f6fa}
.num{position:absolute;width:26px;height:26px;border-radius:50%;background:var(--blue);color:var(--white);font-family:"Montserrat",Arial,sans-serif;font-weight:700;font-size:11px;display:flex;align-items:center;justify-content:center}
.icon{position:absolute;border-radius:50%;background:var(--blue);display:flex;align-items:center;justify-content:center}
</style>
</head>
<body>
<main class="canvas">

  <!-- Hero title slide -->
  <section class="slide hero" style="background:linear-gradient(135deg,#0a2a6e,#1454b8 55%,#0b3585)">
    <div class="abs" role="img" aria-label="Soft glowing network of points and links across the background" style="inset:0;background:radial-gradient(circle at 70% 60%,rgba(90,170,255,.35),transparent 55%),radial-gradient(circle at 20% 80%,rgba(60,140,240,.25),transparent 50%)"></div>
    <div class="logo light" style="left:50%;top:60px;transform:translateX(-50%);font-size:10px"><i style="width:16px;height:16px"></i>Bellwether Guild Forum</div>
    <h1 class="title light" style="position:absolute;left:0;right:0;top:170px;text-align:center;font-size:64px">Bellwether Guild<br>Forum</h1>
    <p class="sub light" style="position:absolute;left:0;right:0;top:330px;text-align:center;font-size:24px">Subtitle of Presentation Goes Here</p>
    <p class="date light" style="position:absolute;left:0;right:0;top:420px;text-align:center;font-size:13px">Wednesday, April 12, 2023</p>
  </section>

  <!-- Row 1 -->
  <section class="slide" style="left:32px;top:788px">
    <svg class="deco" width="560" height="316" viewBox="0 0 560 316" aria-hidden="true">
      <polygon points="380,316 560,140 560,316" fill="var(--blue)"/>
      <polygon points="340,316 360,316 560,120 560,100" fill="var(--navy)"/>
    </svg>
    <div class="logo" style="left:30px;top:22px"><i></i>Bellwether Guild Forum</div>
    <h2 class="title t-lg" style="position:absolute;left:30px;top:92px;width:300px">Presentation Title Goes Here!</h2>
    <p class="sub" style="position:absolute;left:30px;top:168px;width:230px">Subtitle of Presentation Goes Here</p>
    <p class="date" style="position:absolute;left:30px;top:262px">Wednesday, April 12, 2023</p>
    <span class="pager light"></span>
  </section>
  <section class="slide" style="left:608px;top:788px">
    <svg class="deco" width="560" height="316" viewBox="0 0 560 316" aria-hidden="true">
      <rect x="450" y="0" width="110" height="316" fill="var(--blue)"/>
      <rect x="432" y="0" width="10" height="316" fill="var(--navy)"/>
    </svg>
    <div class="logo" style="left:30px;top:22px"><i></i>Bellwether Guild Forum</div>
    <h2 class="title t-lg" style="position:absolute;left:30px;top:92px;width:300px">Presentation Title Goes Here!</h2>
    <p class="sub" style="position:absolute;left:30px;top:168px;width:230px">Subtitle of Presentation Goes Here</p>
    <p class="date" style="position:absolute;left:30px;top:262px">Wednesday, April 12, 2023</p>
    <span class="pager light"></span>
  </section>

  <!-- Row 2 -->
  <section class="slide" style="left:32px;top:1124px">
    <svg class="deco" width="560" height="316" viewBox="0 0 560 316" aria-hidden="true">
      <rect x="0" y="0" width="110" height="316" fill="var(--blue)"/>
      <rect x="118" y="0" width="10" height="316" fill="var(--navy)"/>
    </svg>
    <div class="logo" style="left:200px;top:22px"><i></i>Bellwether Guild Forum</div>
    <h2 class="title t-lg" style="position:absolute;left:200px;top:92px;width:300px">Presentation Title Goes Here!</h2>
    <p class="sub" style="position:absolute;left:200px;top:168px;width:230px">Subtitle of Presentation Goes Here</p>
    <p class="date" style="position:absolute;left:200px;top:262px">Wednesday, April 12, 2023</p>
    <span class="pager"></span>
  </section>
  <section class="slide" style="left:608px;top:1124px">
    <svg class="deco" width="560" height="316" viewBox="0 0 560 316" aria-hidden="true">
      <polygon points="400,0 560,0 560,170" fill="var(--blue)"/>
      <polygon points="360,0 380,0 560,190 560,210" fill="var(--navy)"/>
    </svg>
    <div class="logo" style="left:30px;top:22px"><i></i>Bellwether Guild Forum</div>
    <h2 class="title t-lg" style="position:absolute;left:30px;top:92px;width:300px">Presentation Title Goes Here!</h2>
    <p class="sub" style="position:absolute;left:30px;top:168px;width:230px">Subtitle of Presentation Goes Here</p>
    <p class="date" style="position:absolute;left:30px;top:262px">Wednesday, April 12, 2023</p>
    <span class="pager"></span>
  </section>

  <!-- Row 3 -->
  <section class="slide" style="left:32px;top:1460px;background:var(--blue)">
    <div class="photo ph-tech" role="img" aria-label="Photo of a hand touching glowing digital network icons" style="left:0;top:0;width:250px;height:316px;opacity:.85"></div>
    <div class="logo light" style="left:270px;top:22px"><i></i>Bellwether Guild Forum</div>
    <h2 class="title t-lg light" style="position:absolute;left:270px;top:92px;width:270px">Presentation Title Goes Here!</h2>
    <p class="sub light" style="position:absolute;left:270px;top:168px;width:230px">Subtitle of Presentation Goes Here</p>
    <p class="date light" style="position:absolute;left:270px;top:262px">Wednesday, April 12, 2023</p>
    <span class="pager light"></span>
  </section>
  <section class="slide" style="left:608px;top:1460px;background:linear-gradient(135deg,var(--deep),var(--blue))">
    <svg class="deco" width="560" height="316" viewBox="0 0 560 316" aria-hidden="true">
      <polygon points="380,316 560,130 560,316" fill="rgba(255,255,255,.18)"/>
      <polygon points="350,316 364,316 560,114 560,100" fill="rgba(255,255,255,.8)"/>
    </svg>
    <div class="logo light" style="left:30px;top:22px"><i></i>Bellwether Guild Forum</div>
    <h2 class="title t-lg light" style="position:absolute;left:30px;top:92px;width:300px">Presentation Title Goes Here!</h2>
    <p class="sub light" style="position:absolute;left:30px;top:168px;width:230px">Subtitle of Presentation Goes Here</p>
    <p class="date light" style="position:absolute;left:30px;top:262px">Wednesday, April 12, 2023</p>
    <span class="pager light"></span>
  </section>

  <!-- Row 4 -->
  <section class="slide" style="left:32px;top:1796px;background:linear-gradient(135deg,var(--deep),var(--blue))">
    <svg class="deco" width="560" height="316" viewBox="0 0 560 316" aria-hidden="true">
      <polygon points="0,276 560,236 560,316 0,316" fill="var(--white)"/>
    </svg>
    <div class="logo light" style="left:30px;top:22px"><i></i>Bellwether Guild Forum</div>
    <h2 class="title t-lg light" style="position:absolute;left:30px;top:80px;width:300px">Presentation Title Goes Here!</h2>
    <p class="sub light" style="position:absolute;left:30px;top:156px;width:230px">Subtitle of Presentation Goes Here</p>
    <p class="date light" style="position:absolute;left:30px;top:206px">Wednesday, April 12, 2023</p>
    <span class="pager"></span>
  </section>
  <section class="slide" style="left:608px;top:1796px;background:linear-gradient(135deg,var(--deep),#114aa8)">
    <svg class="deco" width="560" height="316" viewBox="0 0 560 316" aria-hidden="true">
      <rect x="470" y="0" width="90" height="316" fill="rgba(255,255,255,.14)"/>
      <rect x="452" y="0" width="8" height="316" fill="rgba(255,255,255,.8)"/>
    </svg>
    <div class="logo light" style="left:30px;top:22px"><i></i>Bellwether Guild Forum</div>
    <h2 class="title t-lg light" style="position:absolute;left:30px;top:92px;width:300px">Bellwether Guild Forum</h2>
    <p class="sub light" style="position:absolute;left:30px;top:168px;width:230px">Subtitle of Presentation Goes Here</p>
    <p class="date light" style="position:absolute;left:30px;top:262px">Wednesday, April 12, 2023</p>
    <span class="pager light"></span>
  </section>

  <!-- Row 5 -->
  <section class="slide" style="left:32px;top:2132px">
    <svg class="deco" width="560" height="316" viewBox="0 0 560 316" aria-hidden="true">
      <polygon points="0,180 130,316 0,316" fill="var(--blue)"/>
    </svg>
    <span class="abs" style="right:20px;top:20px;width:9px;height:9px;background:var(--blue)"></span>
    <h2 class="title t-md" style="position:absolute;left:24px;top:22px">Table of <span style="color:var(--blue)">Contents</span></h2>
    <div class="num" style="left:170px;top:70px">1</div>
    <p class="item-title" style="position:absolute;left:204px;top:72px">Title Goes Here</p>
    <p class="body" style="position:absolute;left:204px;top:86px;width:140px">Short line of text for this item.</p>
    <div class="num" style="left:170px;top:140px">2</div>
    <p class="item-title" style="position:absolute;left:204px;top:142px">Title Goes Here</p>
    <p class="body" style="position:absolute;left:204px;top:156px;width:140px">Short line of text for this item.</p>
    <div class="num" style="left:170px;top:210px">3</div>
    <p class="item-title" style="position:absolute;left:204px;top:212px">Title Goes Here</p>
    <p class="body" style="position:absolute;left:204px;top:226px;width:140px">Short line of text for this item.</p>
    <div class="num" style="left:370px;top:70px">4</div>
    <p class="item-title" style="position:absolute;left:404px;top:72px">Title Goes Here</p>
    <p class="body" style="position:absolute;left:404px;top:86px;width:130px">Short line of text for this item.</p>
    <div class="num" style="left:370px;top:140px">5</div>
    <p class="item-title" style="position:absolute;left:404px;top:142px">Title Goes Here</p>
    <p class="body" style="position:absolute;left:404px;top:156px;width:130px">Short line of text for this item.</p>
    <div class="num" style="left:370px;top:210px">6</div>
    <p class="item-title" style="position:absolute;left:404px;top:212px">Title Goes Here</p>
    <p class="body" style="position:absolute;left:404px;top:226px;width:130px">Short line of text for this item.</p>
    <span class="pager"></span>
  </section>
  <section class="slide" style="left:608px;top:2132px">
    <div class="photo ph-office" role="img" aria-label="Photo of colleagues meeting around a table" style="left:24px;top:30px;width:226px;height:256px"></div>
    <div class="abs" style="left:250px;top:30px;width:8px;height:256px;background:var(--blue)"></div>
    <p class="item-title" style="position:absolute;left:290px;top:70px;font-size:12px">About</p>
    <h2 class="title t-md" style="position:absolute;left:290px;top:88px;width:240px">Bellwether Guild Forum</h2>
    <p class="body" style="position:absolute;left:290px;top:150px;width:230px">A short paragraph about the forum goes here, with its purpose, members and the work it does each year for the field.</p>
    <p class="body" style="position:absolute;left:290px;top:200px;width:230px">A second short paragraph adds a few more details for readers.</p>
    <span class="pager"></span>
  </section>

  <!-- Row 6 -->
  <section class="slide" style="left:32px;top:2468px">
    <div class="abs" style="right:0;top:0;width:40px;height:316px;background:var(--blue)"></div>
    <h2 class="title t-md" style="position:absolute;left:24px;top:30px">How <span style="color:var(--blue)">We Do It.</span></h2>
    <ul class="body" style="position:absolute;left:36px;top:80px;width:200px;list-style:disc">
      <li>Short bullet text for the first point goes here.</li>
      <li style="margin-top:8px">Short bullet text for the second point goes here.</li>
      <li style="margin-top:8px">Short bullet text for the third point goes here.</li>
    </ul>
    <div class="photo ph-tech" role="img" aria-label="Photo of glowing connected people icons on a digital screen" style="left:260px;top:60px;width:260px;height:170px"></div>
    <span class="pager light"></span>
  </section>
  <section class="slide" style="left:608px;top:2468px">
    <div class="photo ph-hands" role="img" aria-label="Photo of two business people shaking hands" style="left:0;top:0;width:400px;height:316px"></div>
    <div class="abs" style="left:360px;top:40px;width:180px;height:236px;background:var(--white);box-shadow:0 2px 10px rgba(0,0,0,.12)"></div>
    <h2 class="title t-md" style="position:absolute;left:380px;top:62px;width:150px;color:var(--blue)">Slide Title Goes Here!</h2>
    <div class="abs" style="left:360px;top:176px;width:180px;height:100px;background:var(--blue)"></div>
    <div class="icon" style="left:400px;top:190px;width:20px;height:20px;background:var(--white)"></div>
    <p class="item-title light" style="position:absolute;left:375px;top:218px;width:70px;text-align:center">Title Goes Here</p>
    <div class="icon" style="left:480px;top:190px;width:20px;height:20px;background:var(--white)"></div>
    <p class="item-title light" style="position:absolute;left:455px;top:218px;width:70px;text-align:center">Title Goes Here</p>
    <span class="pager"></span>
  </section>

  <!-- Row 7 -->
  <section class="slide" style="left:32px;top:2804px">
    <h2 class="title t-sm" style="position:absolute;left:24px;top:24px;color:var(--blue)">Slide Title <span style="color:var(--navy);font-weight:600">Goes Here!</span></h2>
    <svg class="deco" width="560" height="316" viewBox="0 0 560 316" aria-hidden="true">
      <line x1="220" y1="120" x2="340" y2="120" stroke="var(--line)" stroke-width="2"/>
      <line x1="220" y1="230" x2="340" y2="230" stroke="var(--line)" stroke-width="2"/>
      <line x1="280" y1="90" x2="280" y2="260" stroke="var(--line)" stroke-width="2"/>
      <rect x="270" y="165" width="20" height="20" fill="var(--blue)"/>
    </svg>
    <div class="icon" style="left:196px;top:100px;width:40px;height:40px"><svg width="18" height="18" viewBox="0 0 18 18"><path d="M3 9l4 4 8-8" fill="none" stroke="#fff" stroke-width="2.5"/></svg></div>
    <div class="icon" style="left:324px;top:100px;width:40px;height:40px"><svg width="18" height="18" viewBox="0 0 18 18"><circle cx="8" cy="8" r="5" fill="none" stroke="#fff" stroke-width="2"/><path d="M12 12l4 4" stroke="#fff" stroke-width="2"/></svg></div>
    <div class="icon" style="left:196px;top:210px;width:40px;height:40px"><svg width="18" height="18" viewBox="0 0 18 18"><path d="M2 9h12M10 5l4 4-4 4" fill="none" stroke="#fff" stroke-width="2"/></svg></div>
    <div class="icon" style="left:324px;top:210px;width:40px;height:40px"><svg width="18" height="18" viewBox="0 0 18 18"><path d="M3 15V9M8 15V5M13 15V2" stroke="#fff" stroke-width="2.5"/></svg></div>
    <p class="item-title" style="position:absolute;left:90px;top:104px;width:96px;text-align:right">Title Goes Here</p>
    <p class="body" style="position:absolute;left:60px;top:118px;width:126px;text-align:right">Short text for this point here.</p>
    <p class="item-title" style="position:absolute;left:376px;top:104px">Title Goes Here</p>
    <p class="body" style="position:absolute;left:376px;top:118px;width:126px">Short text for this point here.</p>
    <p class="item-title" style="position:absolute;left:90px;top:214px;width:96px;text-align:right">Title Goes Here</p>
    <p class="body" style="position:absolute;left:60px;top:228px;width:126px;text-align:right">Short text for this point here.</p>
    <p class="item-title" style="position:absolute;left:376px;top:214px">Title Goes Here</p>
    <p class="body" style="position:absolute;left:376px;top:228px;width:126px">Short text for this point here.</p>
    <span class="pager"></span>
  </section>
  <section class="slide" style="left:608px;top:2804px">
    <svg class="deco" width="560" height="316" viewBox="0 0 560 316" aria-hidden="true">
      <polygon points="360,0 560,0 560,230" fill="var(--blue)"/>
      <polygon points="320,0 338,0 560,256 560,276" fill="var(--navy)"/>
    </svg>
    <h2 class="title t-lg" style="position:absolute;left:40px;top:120px;width:260px">Section Braek</h2>
    <p class="body" style="position:absolute;left:40px;top:160px;width:220px">Short line of section text goes here for readers.</p>
    <span class="pager"></span>
  </section>

  <!-- Row 8 -->
  <section class="slide" style="left:32px;top:3140px">
    <h2 class="title t-sm" style="position:absolute;left:24px;top:22px;color:var(--blue)">Slide Title <span style="color:var(--navy);font-weight:600">Goes Here!</span></h2>
    <table class="tbl" style="left:24px;top:56px;width:512px">
      <tr><th>Partner Type</th><th>What They Do</th><th>Main Value</th><th>What We Learn</th></tr>
      <tr><td>Advisor</td><td>Gives input</td><td>Insight</td><td>Trends</td></tr>
      <tr><td>Member Group</td><td>Shares work</td><td>Reach</td><td>Needs</td></tr>
      <tr><td>Program Ally</td><td>Runs events</td><td>Access</td><td>Gaps</td></tr>
      <tr><td>Sponsor</td><td>Funds work</td><td>Support</td><td>Goals</td></tr>
      <tr><td>Research Partner</td><td>Studies data</td><td>Evidence</td><td>Impact</td></tr>
      <tr><td>Network Lead</td><td>Links peers</td><td>Trust</td><td>Reach</td></tr>
      <tr><td>Other</td><td>Helps as needed</td><td>Scale</td><td>Ideas</td></tr>
    </table>
    <span class="pager"></span>
  </section>
  <section class="slide" style="left:608px;top:3140px">
    <h2 class="title t-sm" style="position:absolute;left:24px;top:22px;color:var(--navy);font-weight:600">Partner <b>Complexity</b> and Value Spectrum</h2>
    <svg class="deco" width="560" height="316" viewBox="0 0 560 316" aria-hidden="true">
      <line x1="40" y1="160" x2="520" y2="160" stroke="var(--navy)" stroke-width="2"/>
      <path d="M510 154l10 6-10 6" fill="none" stroke="var(--navy)" stroke-width="2"/>
      <circle cx="80" cy="160" r="6" fill="var(--blue)"/>
      <circle cx="180" cy="160" r="6" fill="var(--blue)"/>
      <circle cx="280" cy="160" r="6" fill="var(--blue)"/>
      <circle cx="380" cy="160" r="6" fill="var(--blue)"/>
      <circle cx="480" cy="160" r="6" fill="var(--blue)"/>
      <rect x="240" y="146" width="80" height="28" rx="14" fill="none" stroke="var(--blue)" stroke-width="2"/>
    </svg>
    <p class="body" style="position:absolute;left:35px;top:122px;width:90px;text-align:center">Low complexity, basic value</p>
    <p class="body" style="position:absolute;left:140px;top:180px;width:80px;text-align:center">Simple ties</p>
    <p class="body" style="position:absolute;left:240px;top:128px;width:80px;text-align:center">Shared work</p>
    <p class="body" style="position:absolute;left:340px;top:180px;width:80px;text-align:center">Joint plans</p>
    <p class="body" style="position:absolute;left:435px;top:122px;width:90px;text-align:center">High complexity, deep value</p>
    <span class="pager"></span>
  </section>

  <!-- Row 9 -->
  <section class="slide" style="left:32px;top:3476px">
    <h2 class="title t-sm" style="position:absolute;left:24px;top:22px;color:var(--blue)">Slide Title <span style="color:var(--navy);font-weight:600">Goes Here!</span></h2>
    <div class="photo ph-desk" role="img" aria-label="Photo of a laptop and papers on a desk" style="left:24px;top:60px;width:245px;height:140px"></div>
    <div class="photo ph-office" role="img" aria-label="Photo of a team working together at a table" style="left:291px;top:60px;width:245px;height:140px"></div>
    <p class="item-title" style="position:absolute;left:24px;top:214px">Title Goes Here</p>
    <p class="body" style="position:absolute;left:24px;top:230px;width:240px">Short text about this image goes here for the reader to see.</p>
    <p class="item-title" style="position:absolute;left:291px;top:214px">Title Goes Here</p>
    <p class="body" style="position:absolute;left:291px;top:230px;width:240px">Short text about this image goes here for the reader to see.</p>
    <span class="pager"></span>
  </section>
  <section class="slide" style="left:608px;top:3476px">
    <div class="abs" style="right:0;top:0;width:60px;height:316px;background:var(--blue)"></div>
    <h2 class="title t-sm" style="position:absolute;left:24px;top:22px;color:var(--blue)">Slide Title <span style="color:var(--navy);font-weight:600">Goes Here!</span></h2>
    <div class="photo ph-desk" role="img" aria-label="Photo of hands writing notes beside a laptop" style="left:300px;top:60px;width:220px;height:200px"></div>
    <p class="item-title" style="position:absolute;left:24px;top:70px">Title Goes Here</p>
    <p class="body" style="position:absolute;left:24px;top:86px;width:250px">A short paragraph goes here with a few lines of text about the topic of this slide.</p>
    <ul class="body" style="position:absolute;left:36px;top:140px;width:240px;list-style:disc">
      <li>Short bullet point one.</li>
      <li>Short bullet point two.</li>
      <li>Short bullet point three.</li>
      <li>Short bullet point four.</li>
    </ul>
    <span class="pager light"></span>
  </section>

  <!-- Row 10 -->
  <section class="slide" style="left:32px;top:3812px">
    <div class="abs" style="left:200px;top:0;width:160px;height:316px;background:var(--blue)"></div>
    <div class="abs" style="left:220px;top:98px;width:120px;height:120px;border-radius:50%;border:3px solid var(--white)"></div>
    <h2 class="title light" style="position:absolute;left:230px;top:138px;width:100px;text-align:center;font-size:15px">Slide Title Goes Here!</h2>
    <div class="icon" style="left:170px;top:60px;width:28px;height:28px;border:2px solid #fff"></div>
    <div class="icon" style="left:362px;top:60px;width:28px;height:28px;border:2px solid #fff"></div>
    <div class="icon" style="left:170px;top:220px;width:28px;height:28px;border:2px solid #fff"></div>
    <div class="icon" style="left:362px;top:220px;width:28px;height:28px;border:2px solid #fff"></div>
    <p class="item-title" style="position:absolute;left:40px;top:58px;width:120px;text-align:right;font-size:12px">Title Goes Here</p>
    <p class="body" style="position:absolute;left:40px;top:90px;width:120px;text-align:right">Short text for this point.</p>
    <p class="item-title" style="position:absolute;left:400px;top:58px;width:120px;font-size:12px">Title Goes Here</p>
    <p class="body" style="position:absolute;left:400px;top:90px;width:120px">Short text for this point.</p>
    <p class="item-title" style="position:absolute;left:40px;top:218px;width:120px;text-align:right;font-size:12px">Title Goes Here</p>
    <p class="body" style="position:absolute;left:40px;top:250px;width:120px;text-align:right">Short text for this point.</p>
    <p class="item-title" style="position:absolute;left:400px;top:218px;width:120px;font-size:12px">Title Goes Here</p>
    <p class="body" style="position:absolute;left:400px;top:250px;width:120px">Short text for this point.</p>
    <span class="pager"></span>
  </section>
  <section class="slide" style="left:608px;top:3812px">
    <h2 class="title t-sm" style="position:absolute;left:24px;top:22px;color:var(--blue)">Slide Title <span style="color:var(--navy);font-weight:600">Goes Here!</span></h2>
    <svg class="deco" width="560" height="316" viewBox="0 0 560 316" aria-hidden="true">
      <line x1="90" y1="110" x2="470" y2="110" stroke="var(--line)" stroke-width="2"/>
      <g fill="var(--white)" stroke="var(--navy)" stroke-width="3">
        <circle cx="90" cy="110" r="26"/><circle cx="217" cy="110" r="26"/><circle cx="343" cy="110" r="26"/><circle cx="470" cy="110" r="26"/>
      </g>
      <g font-family="Montserrat, Arial, sans-serif" font-weight="700" font-size="18" fill="var(--navy)" text-anchor="middle">
        <text x="90" y="117">1</text><text x="217" y="117">2</text><text x="343" y="117">3</text><text x="470" y="117">4</text>
      </g>
    </svg>
    <p class="item-title" style="position:absolute;left:50px;top:150px;width:80px;text-align:center;font-size:12px">Title Goes Here</p>
    <p class="body" style="position:absolute;left:45px;top:186px;width:90px;text-align:center">Short text for this step goes here.</p>
    <p class="item-title" style="position:absolute;left:177px;top:150px;width:80px;text-align:center;font-size:12px">Title Goes Here</p>
    <p class="body" style="position:absolute;left:172px;top:186px;width:90px;text-align:center">Short text for this step goes here.</p>
    <p class="item-title" style="position:absolute;left:303px;top:150px;width:80px;text-align:center;font-size:12px">Title Goes Here</p>
    <p class="body" style="position:absolute;left:298px;top:186px;width:90px;text-align:center">Short text for this step goes here.</p>
    <p class="item-title" style="position:absolute;left:430px;top:150px;width:80px;text-align:center;font-size:12px">Title Goes Here</p>
    <p class="body" style="position:absolute;left:425px;top:186px;width:90px;text-align:center">Short text for this step goes here.</p>
    <span class="pager"></span>
  </section>

  <!-- Row 11 -->
  <section class="slide" style="left:32px;top:4148px">
    <h2 class="title t-sm" style="position:absolute;left:24px;top:22px;color:var(--blue)">Slide Title <span style="color:var(--navy);font-weight:600">Goes Here!</span></h2>
    <p class="body" style="position:absolute;left:280px;top:26px;width:250px">A short line of chart notes goes here for readers.</p>
    <svg class="deco" width="560" height="316" viewBox="0 0 560 316" aria-hidden="true">
      <line x1="30" y1="280" x2="260" y2="280" stroke="var(--line)"/>
      <line x1="30" y1="80" x2="30" y2="280" stroke="var(--line)"/>
      <g fill="var(--navy)">
        <rect x="40" y="180" width="10" height="100"/><rect x="76" y="140" width="10" height="140"/><rect x="112" y="200" width="10" height="80"/><rect x="148" y="110" width="10" height="170"/><rect x="184" y="160" width="10" height="120"/><rect x="220" y="100" width="10" height="180"/>
      </g>
      <g fill="var(--sky)">
        <rect x="52" y="210" width="10" height="70"/><rect x="88" y="170" width="10" height="110"/><rect x="124" y="150" width="10" height="130"/><rect x="160" y="190" width="10" height="90"/><rect x="196" y="130" width="10" height="150"/><rect x="232" y="150" width="10" height="130"/>
      </g>
    </svg>
    <table class="tbl" style="left:280px;top:70px;width:256px">
      <tr><th>Item</th><th>Q1</th><th>Q2</th><th>Q3</th></tr>
      <tr><td>Row Name Here</td><td>2.4</td><td>3.1</td><td>4.0</td></tr>
      <tr><td>Row Name Here</td><td>1.8</td><td>2.6</td><td>3.3</td></tr>
      <tr><td>Row Name Here</td><td>3.2</td><td>2.9</td><td>3.8</td></tr>
      <tr><td>Row Name Here</td><td>2.1</td><td>3.5</td><td>4.2</td></tr>
      <tr><td>Row Name Here</td><td>2.7</td><td>3.0</td><td>3.6</td></tr>
    </table>
    <span class="pager"></span>
  </section>
  <section class="slide" style="left:608px;top:4148px;background:var(--blue)">
    <div class="photo ph-blue" role="img" aria-label="Blue-toned photo of business people shaking hands" style="inset:0;opacity:.9"></div>
    <h2 class="title t-md light" style="position:absolute;left:300px;top:150px">Contact Us</h2>
    <div class="icon" style="left:300px;top:188px;width:14px;height:14px;background:var(--white)"></div>
    <p class="body light" style="position:absolute;left:320px;top:190px">+1 555 010 2030</p>
    <div class="icon" style="left:300px;top:210px;width:14px;height:14px;background:var(--white)"></div>
    <p class="body light" style="position:absolute;left:320px;top:212px">hello@bellwetherguild.org</p>
    <div class="icon" style="left:300px;top:232px;width:14px;height:14px;background:var(--white)"></div>
    <p class="body light" style="position:absolute;left:320px;top:234px">www.bellwetherguild.org</p>
    <span class="pager light"></span>
  </section>

</main>
</body>
</html>
```